Industrial Professional Business Card Design (Vantrel Systems)

Would like professional looking business cards. Not too busy leaning towards minimal. Should have a slogan like:
"Industrial Automation and Control".

We are a tech company that programs industrial PLC computers. We also develop custom hardware solutions. Please use the logo for inspiration.

Target Market(s)

Mining, industrial, processing, automation, factory

Industry/Entity Type

Engineering

Contact Information for Business Card

Name, phone, email, website. job title.

Font styles to use
Other font styles liked:
• droid sans

Requirements
Must have
• Use colours that go well with the logo. Not too busy design.

```html
<!DOCTYPE html>
<html lang="en">
<head>
<meta charset="utf-8">
<title>Vantrel Systems — Business Card</title>
<link href="https://fonts.googleapis.com/css2?family=Noto+Sans:wght@400;700&display=swap" rel="stylesheet">
<style>
  :root {
    --navy: #0f4374;
    --navy-text: #1d3f66;
    --orange: #f26a21;
    --bg-light: #ffffff;
    --bg-edge: #d9d9d9;
    --white: #ffffff;
  }
  html, body {
    margin: 0;
    padding: 0;
    overflow: hidden;
    background: #ececec;
  }
  .card {
    position: relative;
    width: 1200px;
    height: 686px;
    overflow: hidden;
    background: radial-gradient(ellipse 70% 60% at 50% 25%, var(--bg-light) 0%, #f1f1f1 55%, var(--bg-edge) 100%);
    font-family: "Noto Sans", "Droid Sans", sans-serif;
  }
  .card__bands {
    position: absolute;
    inset: 0;
    width: 1200px;
    height: 686px;
  }
  .brand {
    position: absolute;
    top: 236px;
    left: 0;
    width: 1200px;
    display: flex;
    justify-content: center;
    align-items: center;
    gap: 20px;
  }
  .brand__dot {
    width: 30px;
    height: 30px;
    border-radius: 50%;
    background: var(--orange);
  }
  .brand__name {
    margin: 0;
    font-size: 64px;
    font-weight: 400;
    line-height: 1;
    color: var(--navy-text);
    letter-spacing: 0.5px;
  }
  .slogan {
    position: absolute;
    top: 384px;
    left: 0;
    width: 1200px;
    margin: 0;
    text-align: center;
    font-size: 56px;
    font-weight: 700;
    color: var(--white);
    letter-spacing: 1px;
    line-height: 1;
  }
  .person {
    position: absolute;
    top: 520px;
    left: 0;
    width: 1200px;
    text-align: center;
    color: var(--orange);
  }
  .person__name {
    margin: 0;
    font-size: 41px;
    font-weight: 700;
    line-height: 1.1;
  }
  .person__title {
    margin: 0;
    font-size: 30px;
    font-weight: 400;
    line-height: 1.2;
  }
  .contacts {
    position: absolute;
    top: 620px;
    left: 58px;
    right: 58px;
    display: flex;
    justify-content: space-between;
    align-items: center;
  }
  .contact {
    display: flex;
    align-items: center;
    gap: 10px;
    font-size: 28px;
    line-height: 1.2;
    color: var(--navy-text);
    white-space: nowrap;
  }
  .contact svg { flex: none; }
</style>
</head>
<body>
  <div class="card">
    <svg class="card__bands" viewBox="0 0 1200 686" aria-hidden="true">
      <path class="band band--orange" fill="var(--orange)"
            d="M0,238 Q600,448 1200,240 L1200,590 Q600,411 0,600 Z"/>
      <path class="band band--navy" fill="var(--navy)"
            d="M0,269 Q600,439 1200,257 L1200,560 Q600,393 0,566 Z"/>
      <path class="band-edge" fill="none" stroke="var(--white)" stroke-width="3"
            d="M0,270 Q600,440 1200,258"/>
      <path class="band-edge" fill="none" stroke="var(--white)" stroke-width="4"
            d="M0,568 Q600,395 1200,562"/>
    </svg>

    <div class="brand">
      <span class="brand__dot"></span>
      <p class="brand__name">Vantrel Systems</p>
    </div>

    <h1 class="slogan">Industrial Automation and Control</h1>

    <div class="person">
      <p class="person__name">Business Name</p>
      <p class="person__title">Job Title</p>
    </div>

    <div class="contacts">
      <div class="contact contact--phone">
        <svg width="28" height="28" viewBox="0 0 24 24" aria-hidden="true">
          <path fill="var(--navy-text)" d="M6.6 10.8c1.4 2.8 3.8 5.1 6.6 6.6l2.2-2.2c.3-.3.7-.4 1-.2 1.1.4 2.3.6 3.6.6.6 0 1 .4 1 1V20c0 .6-.4 1-1 1C10.6 21 3 13.4 3 4c0-.6.4-1 1-1h3.5c.6 0 1 .4 1 1 0 1.3.2 2.5.6 3.6.1.3 0 .7-.2 1z"/>
          <path fill="none" stroke="var(--navy-text)" stroke-width="1.6" stroke-linecap="round" d="M14 3.5a6.5 6.5 0 0 1 6.5 6.5M14 7a3 3 0 0 1 3 3"/>
        </svg>
        <span>+00 4821 3907 5516</span>
      </div>

      <div class="contact contact--email">
        <svg width="26" height="20" viewBox="0 0 26 20" aria-hidden="true">
          <rect x="1" y="3" width="24" height="15" fill="var(--navy-text)"/>
          <path fill="none" stroke="var(--white)" stroke-width="1.8" d="M1.5 3.5 13 12 24.5 3.5"/>
        </svg>
        <span>info@vantrel.com</span>
      </div>

      <div class="contact contact--web">
        <svg width="28" height="28" viewBox="0 0 24 24" aria-hidden="true">
          <g fill="none" stroke="var(--navy-text)" stroke-width="1.6">
            <circle cx="12" cy="12" r="10"/>
            <ellipse cx="12" cy="12" rx="4.5" ry="10"/>
            <path d="M2 12h20M4 6.5h16M4 17.5h16"/>
          </g>
        </svg>
        <span>www.vantrel.com</span>
      </div>
    </div>
  </div>
</body>
</html>
```